Design PPT/website graphic of a Smart Building consisting 8 components

For a new PPT presentation and also for use on the website, we want to develop a graphical model of a Smart Building (modern office building) where the 8 components of our proposition are visualized both individually and as a whole.
Details, extra information, styles etc. are all in the attached files
Updates

I start to get more dedigns, but since pixelforum advice met to change to the ppt category I get now more complete ppt designs while my initial brief ask for a 8 component building, so I like to blend the initial task of designing a 8 component smart building and a ppt slide deck. I will give detailed feedback on every proposed design. Thank you

```html
<!DOCTYPE html>
<html lang="en">
<head>
<meta charset="utf-8">
<title>Smart Building – Eight Components</title>
<link href="https://fonts.googleapis.com/css2?family=Poppins:wght@400;600;700&display=swap" rel="stylesheet">
<style>
  :root{
    --backdrop:#dcdcdc;
    --sheet:#ffffff;
    --roof-dark:#335e24;
    --roof-green:#4f8a32;
    --roof-stripe:#6db544;
    --chimney-cap:#0f3317;
    --chimney:#15501f;
    --icon:#6db544;
    --ink:#2f3b3a;
    --ink-soft:#3c4645;
    --card-grey:#f1f1f1;
    --tint-1:#e1efda;
    --tint-2:#c4e3b4;
    --tint-3:#a5d48a;
    --slate:#67787a;
  }
  *{box-sizing:border-box;margin:0;padding:0}
  html,body{width:1010px;height:1200px;overflow:hidden}
  body{background:var(--backdrop);font-family:"Poppins",sans-serif;color:var(--ink);position:relative}

  .slide{position:absolute;left:42px;width:925px;height:521px;background:var(--sheet)}
  .slide--grey{top:56px}
  .slide--tinted{top:623px}

  .roof{position:absolute;left:0;top:0;width:925px;height:183px}
  .brand{position:absolute;left:465px;top:108px;transform:translate(-50%,-50%);display:flex;align-items:center;gap:4px;
    color:#fff;font-weight:600;font-size:9px;letter-spacing:.5px;white-space:nowrap}
  .brand__dot{width:7px;height:7px;border-radius:50%;background:#fff}
  .title{position:absolute;left:0;width:925px;top:128px;text-align:center;color:#fff;font-weight:700;font-size:23px;line-height:34px}

  .card{position:absolute;display:flex;align-items:center;background:var(--card-grey)}
  .card h3{font-weight:700;font-size:10.6px;line-height:13px;color:var(--ink)}
  .card p{font-size:7.6px;line-height:9.3px;color:var(--ink-soft)}
  .icon{position:absolute;width:33px;height:33px;border-radius:50%;background:var(--icon);display:flex;align-items:center;justify-content:center}
  .icon svg{width:21px;height:21px;fill:none;stroke:#fff;stroke-width:1.3;stroke-linecap:round;stroke-linejoin:round}

  .card--left{left:101px;width:242px;height:84px}
  .card--left .text{position:absolute;right:44px;width:192px;text-align:right}
  .card--left .icon{right:6px;top:8px}
  .card--right{left:586px;width:243px;height:84px}
  .card--right .text{position:absolute;left:48px;width:193px}
  .card--right .icon{left:8px;top:8px}
  .row-1{top:180px}.row-2{top:270px}.row-3{top:360px}

  .card--centre{left:349px;top:180px;width:232px;height:264px;flex-direction:column;justify-content:center;text-align:center}
  .card--centre .icon{position:static;width:46px;height:46px;margin-bottom:7px}
  .card--centre .icon svg{width:28px;height:28px}
  .card--centre h3{font-size:11.5px;line-height:14px}
  .card--centre p{font-size:9.4px;line-height:11.6px;width:204px}

  .card--base{left:101px;top:450px;width:727px;height:56px}
  .card--base .icon{left:36px;top:12px}
  .card--base .text{position:absolute;left:80px}
  .card--base h3{font-size:12px;line-height:13px}
  .card--base p{font-size:9.6px;line-height:11.8px}

  .slide--tinted .tint-1{background:var(--tint-1)}
  .slide--tinted .tint-2{background:var(--tint-2)}
  .slide--tinted .tint-3{background:var(--tint-3)}
  .slide--tinted .card--base{background:var(--slate)}
  .slide--tinted .card--base h3,.slide--tinted .card--base p{color:#fff}
</style>
</head>
<body>

<svg width="0" height="0" style="position:absolute">
  <defs>
    <g id="g-sensor"><circle cx="12" cy="12" r="2"/><path d="M8.5 8.5a5 5 0 0 0 0 7M15.5 8.5a5 5 0 0 1 0 7M6 6a8.5 8.5 0 0 0 0 12M18 6a8.5 8.5 0 0 1 0 12"/></g>
    <g id="g-collect"><rect x="4" y="4" width="4" height="5"/><rect x="10" y="4" width="4" height="5"/><rect x="16" y="4" width="4" height="5"/><path d="M6 9v3h12V9M12 12v2"/><ellipse cx="12" cy="15.5" rx="3" ry="1.3"/><path d="M9 15.5v4c0 .8 6 .8 6 0v-4"/></g>
    <g id="g-connect"><circle cx="12" cy="12" r="4"/><path d="M8 12h8M12 8v8"/><circle cx="4" cy="12" r="1.3"/><circle cx="20" cy="12" r="1.3"/><circle cx="12" cy="4" r="1.3"/><circle cx="12" cy="20" r="1.3"/><circle cx="5.5" cy="5.5" r="1.3"/><circle cx="18.5" cy="18.5" r="1.3"/><path d="M5.3 12H8M16 12h2.7M12 5.3V8M12 16v2.7M6.5 6.5l2.7 2.7M14.8 14.8l2.7 2.7"/></g>
    <g id="g-network"><rect x="9.5" y="3" width="5" height="4"/><path d="M12 7v3M5 10h14M5 10v3M12 10v3M19 10v3"/><rect x="3" y="13" width="4" height="3"/><rect x="10" y="13" width="4" height="3"/><rect x="17" y="13" width="4" height="3"/><path d="M3 18h4M10 18h4M17 18h4M3 20h4M10 20h4M17 20h4"/></g>
    <g id="g-shield"><path d="M12 3l7 3v5c0 5-3.5 8-7 10-3.5-2-7-5-7-10V6z"/><rect x="9.5" y="11" width="5" height="4"/><path d="M10.5 11V9.5a1.5 1.5 0 0 1 3 0V11"/></g>
    <g id="g-storage"><ellipse cx="10" cy="5.5" rx="5" ry="2"/><path d="M5 5.5v9c0 1 2.2 2 5 2M15 5.5V10M5 10c0 1 2.2 2 5 2"/><path d="M12 13h8v7h-8z"/><path d="M12 13l4 3.5 4-3.5"/></g>
    <g id="g-integrate"><rect x="7" y="7" width="10" height="10" rx="1"/><circle cx="12" cy="12" r="2.5"/><path d="M9 4v3M12 4v3M15 4v3M9 17v3M12 17v3M15 17v3M4 9h3M4 12h3M4 15h3M17 9h3M17 12h3M17 15h3"/></g>
    <g id="g-home"><path d="M4 11l8-7 8 7M6 9.5V20h12V9.5"/><circle cx="12" cy="15" r="3"/><path d="M12 12v2.5"/><path d="M15.5 5.5a2.5 2.5 0 0 1 3 3"/></g>
  </defs>
</svg>

<!-- ===== Variant A : neutral grey panels ===== -->
<section class="slide slide--grey">
  <svg class="roof" viewBox="0 0 1615 320" aria-hidden="true">
    <rect x="1095" y="100" width="81" height="24" rx="3" fill="var(--chimney-cap)"/>
    <rect x="1103" y="124" width="66" height="45" fill="var(--chimney)"/>
    <path d="M66 224L177 212M1447 212L1548 224" stroke="var(--roof-dark)" stroke-width="4"/>
    <polygon points="177,207 812,117 1447,207 1447,232 812,145 177,232" fill="var(--roof-dark)"/>
    <polygon points="177,232 812,145 1447,232 1447,296 177,296" fill="var(--roof-green)"/>
    <rect x="177" y="295" width="1270" height="7" fill="var(--roof-stripe)"/>
  </svg>
  <div class="brand"><span class="brand__dot"></span>Quorrin</div>
  <h1 class="title">Smart Building</h1>

  <article class="card card--left row-1"><div class="text"><h3>Sensor Network</h3><p>Data is collected using a fine-mesh network of (multi)sensors. This data covers all aspects of the building, including technical installations, users, usage patterns, and the environment.</p></div><span class="icon"><svg viewBox="0 0 24 24"><use href="#g-sensor"/></svg></span></article>
  <article class="card card--left row-2"><div class="text"><h3>Data Collection</h3><p>Data is processed into information, leading to insights for improving building efficiency. In case of detected deviations, corrective actions are automatically triggered.</p></div><span class="icon"><svg viewBox="0 0 24 24"><use href="#g-collect"/></svg></span></article>
  <article class="card card--left row-3"><div class="text"><h3>Connectivity</h3><p>Within a Smart Building, many different products and systems are installed that produce data. It is important that these communicate and collect data in a uniform manner, without the need for various protocol converters. This interoperability is essential for optimal building operation.</p></div><span class="icon"><svg viewBox="0 0 24 24"><use href="#g-connect"/></svg></span></article>

  <article class="card card--centre"><span class="icon"><svg viewBox="0 0 24 24"><use href="#g-network"/></svg></span><h3>IT Network</h3><p>A professional IT infrastructure is necessary to quickly and securely transport data within the building and to/from the Cloud. Such a structure includes managed switches, (redundant) fiber optic cabling, cybersecurity, and Cloud solutions.</p></article>

  <article class="card card--right row-1"><span class="icon"><svg viewBox="0 0 24 24"><use href="#g-shield"/></svg></span><div class="text"><h3>Cybersecurity</h3><p>A professional and controlled cyber security solution is required for the collection, transportation, security, storage, manipulation, processing, and sharing of data. This applies both within the building itself and for data traveling to and from the Cloud and external data centers.</p></div></article>
  <article class="card card--right row-2"><span class="icon"><svg viewBox="0 0 24 24"><use href="#g-storage"/></svg></span><div class="text"><h3>Data Storage</h3><p>Due to the heavy reliance on data, it is essential for the continuity and security of a Smart Building to establish what is known as an independent data layer. This layer stores and processes data regardless of the sensor or device that generates it.</p></div></article>
  <article class="card card--right row-3"><span class="icon"><svg viewBox="0 0 24 24"><use href="#g-integrate"/></svg></span><div class="text"><h3>Third-party Integration Solutions</h3><p>Building automation, data solutions, IT networks, and cybersecurity solutions are provided by Quorrin as integrated solutions. We also deliver seamless integrations with third-party solutions.</p></div></article>

  <article class="card card--base"><span class="icon"><svg viewBox="0 0 24 24"><use href="#g-home"/></svg></span><div class="text"><h3>Building Automation</h3><p>The automation of the cooling, heating, ventilation, and lighting systems forms the basis of every Smart Building.<br>This foundational system consists of sensors, actuators, network and room controllers, and a building management system (BMS).</p></div></article>
</section>

<!-- ===== Variant B : green tints with slate foundation ===== -->
<section class="slide slide--tinted">
  <svg class="roof" viewBox="0 0 1615 320" aria-hidden="true">
    <rect x="1095" y="100" width="81" height="24" rx="3" fill="var(--chimney-cap)"/>
    <rect x="1103" y="124" width="66" height="45" fill="var(--chimney)"/>
    <path d="M66 224L177 212M1447 212L1548 224" stroke="var(--roof-dark)" stroke-width="4"/>
    <polygon points="177,207 812,117 1447,207 1447,232 812,145 177,232" fill="var(--roof-dark)"/>
    <polygon points="177,232 812,145 1447,232 1447,296 177,296" fill="var(--roof-green)"/>
    <rect x="177" y="295" width="1270" height="7" fill="var(--roof-stripe)"/>
  </svg>
  <div class="brand"><span class="brand__dot"></span>Quorrin</div>
  <h1 class="title">Smart Building</h1>

  <article class="card card--left row-1 tint-1"><div class="text"><h3>Sensor Network</h3><p>Data is collected using a fine-mesh network of (multi)sensors. This data covers all aspects of the building, including technical installations, users, usage patterns, and the environment.</p></div><span class="icon"><svg viewBox="0 0 24 24"><use href="#g-sensor"/></svg></span></article>
  <article class="card card--left row-2 tint-2"><div class="text"><h3>Data Collection</h3><p>Data is processed into information, leading to insights for improving building efficiency. In case of detected deviations, corrective actions are automatically triggered.</p></div><span class="icon"><svg viewBox="0 0 24 24"><use href="#g-collect"/></svg></span></article>
  <article class="card card--left row-3 tint-3"><div class="text"><h3>Connectivity</h3><p>Within a Smart Building, many different products and systems are installed that produce data. It is important that these communicate and collect data in a uniform manner, without the need for various protocol converters. This interoperability is essential for optimal building operation.</p></div><span class="icon"><svg viewBox="0 0 24 24"><use href="#g-connect"/></svg></span></article>

  <article class="card card--centre tint-1"><span class="icon"><svg viewBox="0 0 24 24"><use href="#g-network"/></svg></span><h3>IT Network</h3><p>A professional IT infrastructure is necessary to quickly and securely transport data within the building and to/from the Cloud. Such a structure includes managed switches, (redundant) fiber optic cabling, cybersecurity, and Cloud solutions.</p></article>

  <article class="card card--right row-1 tint-1"><span class="icon"><svg viewBox="0 0 24 24"><use href="#g-shield"/></svg></span><div class="text"><h3>Cybersecurity</h3><p>A professional and controlled cyber security solution is required for the collection, transportation, security, storage, manipulation, processing, and sharing of data. This applies both within the building itself and for data traveling to and from the Cloud and external data centers.</p></div></article>
  <article class="card card--right row-2 tint-2"><span class="icon"><svg viewBox="0 0 24 24"><use href="#g-storage"/></svg></span><div class="text"><h3>Data Storage</h3><p>Due to the heavy reliance on data, it is essential for the continuity and security of a Smart Building to establish what is known as an independent data layer. This layer stores and processes data regardless of the sensor or device that generates it.</p></div></article>
  <article class="card card--right row-3 tint-3"><span class="icon"><svg viewBox="0 0 24 24"><use href="#g-integrate"/></svg></span><div class="text"><h3>Third-party Integration Solutions</h3><p>Building automation, data solutions, IT networks, and cybersecurity solutions are provided by Quorrin as integrated solutions. We also deliver seamless integrations with third-party solutions.</p></div></article>

  <article class="card card--base"><span class="icon"><svg viewBox="0 0 24 24"><use href="#g-home"/></svg></span><div class="text"><h3>Building Automation</h3><p>The automation of the cooling, heating, ventilation, and lighting systems forms the basis of every Smart Building.<br>This foundational system consists of sensors, actuators, network and room controllers, and a building management system (BMS).</p></div></article>
</section>

</body>
</html>
```